Menu Re-Design for The Marlowbrook a british eatery in spanish holiday resort

Looking for a new design for our breakfast and lunch menu....

I have included some pictures of a few menus I like the feel of File No 1,2,3,4,5..... but am open to any ideas you may have....

The menu is to be double sided consisting of a front design with actual menu on reverse....

I have also included the relevant text files you will require...

We do not have a logo or set colour scheme to follow...

Target Market(s)

Predominantly British holidaymakers in popular Spanish resort....

Requirements
Must have
• Menu to be A3 and double sided, split between either a front page design and menu on reverse, or menu divided between both sides....
• Company Name:- The Marlowbrook
Nice to have
• Fun and Bold design whilst maintaining a feel of quality....
Should not have
• Please avoid the use of any food photography....

```html
<!DOCTYPE html>
<html lang="en">
<head>
<meta charset="utf-8">
<title>The Marlowbrook – Breakfast &amp; Lunch Menu</title>
<link href="https://fonts.googleapis.com/css2?family=Montserrat:ital,wght@0,700;0,800;1,700&family=Open+Sans:ital,wght@0,400;0,600;0,700;1,600&display=swap" rel="stylesheet">
<style>
  :root {
    --pink: #ef3a5d;
    --pink-soft: #f2506e;
    --pink-deep: #c2274a;
    --yellow: #f9d71c;
    --yellow-ink: #8c7a12;
    --teal: #4fd8d6;
    --teal-ink: #2a9fa0;
    --teal-text: #35b7b5;
    --ink: #4a4a4a;
    --rule: #d6d6d6;
    --panel: #f3f3f3;
    --paper: #ffffff;
    --paper-soft: #fafafa;
    --deco: #e4e4e4;
  }
  * { margin: 0; padding: 0; box-sizing: border-box; }
  html, body { width: 849px; height: 1200px; overflow: hidden; background: var(--paper); }
  body { font-family: "Open Sans", sans-serif; color: var(--ink); }
  .menu { position: relative; width: 849px; height: 1200px; overflow: hidden; background: var(--paper); }
  .abs { position: absolute; }

  /* Masthead */
  .masthead { position: absolute; left: 0; top: 0; width: 849px; height: 198px; background: var(--pink); }
  .masthead__right { position: absolute; left: 424px; top: 0; width: 425px; height: 198px; background: var(--pink-soft); border-left: 2px dashed rgba(255,255,255,.7); }
  .brand { position: absolute; left: 36px; top: 40px; font-family: "Montserrat", sans-serif; font-weight: 800; line-height: 1; }
  .brand__the { display: block; font-size: 66px; color: #fff; }
  .brand__name { display: block; font-size: 44px; margin-top: 10px; letter-spacing: -0.5px; color: var(--pink-deep); }
  .pan-art { position: absolute; left: 196px; top: 14px; width: 140px; height: 94px; border-radius: 14px; background: linear-gradient(135deg, #f7d9c4, #2b2b2b); opacity: .85; }
  .headline { position: absolute; left: 470px; top: 26px; font-family: "Montserrat", sans-serif; font-weight: 800; color: var(--yellow); font-size: 49px; line-height: 52px; letter-spacing: -0.5px; }
  .headline .amp { color: var(--pink-deep); }
  .served { position: absolute; left: 472px; top: 138px; width: 306px; height: 34px; background: var(--teal); color: #fff; font-size: 25px; line-height: 34px; text-align: center; letter-spacing: .5px; }
  .plate-art { position: absolute; left: 738px; top: 44px; width: 88px; height: 86px; border-radius: 50%; background: radial-gradient(circle, #f4b37a 0 45%, #ffffff 46%); }

  /* Column heads */
  .col-head { position: absolute; top: 198px; height: 84px; background: var(--teal); }
  .col-head h2 { font-family: "Montserrat", sans-serif; font-weight: 800; color: var(--teal-ink); font-size: 37px; position: absolute; }
  .col-head--breakfast { left: 0; width: 294px; }
  .col-head--breakfast h2 { left: 24px; top: 18px; }
  .col-head--snacks { left: 582px; width: 267px; }
  .col-head--snacks h2 { left: 26px; top: 22px; }
  .col-head--build { left: 294px; width: 288px; height: 108px; background: var(--yellow); }
  .col-head--build h2 { color: var(--yellow-ink); width: 100%; text-align: center; top: 12px; font-size: 36px; line-height: 38px; }
  .icon-art { position: absolute; background: rgba(255,255,255,.35); border-radius: 8px; }

  /* Build panel */
  .build-panel { position: absolute; left: 294px; top: 306px; width: 288px; height: 426px; background: var(--panel); }

  .list { position: absolute; list-style: none; font-size: 11.5px; }
  .list li { display: flex; justify-content: space-between; align-items: center; }
  .list .price { font-weight: 700; }
  .list--build { left: 322px; top: 318px; width: 227px; }
  .list--build li { height: 26px; }
  .list--snacks { left: 611px; top: 313px; width: 209px; }
  .list--snacks li { height: 28.4px; }

  .min-order { position: absolute; left: 330px; top: 676px; width: 215px; height: 37px; background: var(--yellow); box-shadow: 2px 2px 0 #d9d9d9; color: var(--yellow-ink); font-style: italic; font-weight: 700; font-size: 16px; line-height: 37px; text-align: center; }

  /* Breakfast column */
  .intro { position: absolute; left: 17px; top: 304px; width: 265px; font-size: 12px; line-height: 21px; }
  .set-name { position: absolute; left: 17px; font-weight: 700; color: var(--teal-text); font-size: 15.5px; }
  .set-desc { position: absolute; left: 17px; width: 242px; font-size: 11.5px; line-height: 17.6px; }
  .set-free { position: absolute; left: 17px; font-weight: 700; color: var(--teal-text); font-size: 15.5px; }
  .set-drink { position: absolute; left: 17px; width: 256px; display: flex; justify-content: space-between; font-size: 11.5px; }
  .set-drink .price { font-weight: 700; }
  .divider { position: absolute; left: 17px; top: 517px; width: 259px; border-top: 1px dashed var(--rule); }
  .note { position: absolute; left: 16px; top: 662px; width: 260px; font-style: italic; font-weight: 600; color: var(--teal-text); font-size: 11.5px; line-height: 18px; }

  /* Specials */
  .specials { position: absolute; left: 0; top: 732px; width: 849px; height: 468px; background: var(--paper-soft); border-top: 1px solid #eee; }
  .banner { position: absolute; left: 245px; top: 780px; width: 360px; height: 46px; background: var(--pink); box-shadow: 2px 2px 0 #d0d0d0; color: #fff; font-family: "Montserrat", sans-serif; font-weight: 700; font-size: 27px; line-height: 46px; text-align: center; }
  .split { position: absolute; left: 424px; top: 854px; height: 302px; border-left: 1px dashed var(--pink); }
  .dish { position: absolute; }
  .dish h3 { font-weight: 700; color: var(--pink); font-size: 15.5px; margin-bottom: 9px; }
  .dish__body { display: flex; justify-content: space-between; font-size: 11.5px; line-height: 17.6px; }
  .dish__body p { width: 275px; }
  .dish__body .price { font-weight: 700; }
  .dish--left { left: 62px; width: 340px; }
  .dish--right { left: 448px; width: 341px; }
  .dish--right .dish__body p { width: 290px; }
  .aside { display: block; font-weight: 600; }
  .deco { position: absolute; background: var(--deco); border-radius: 50%; opacity: .7; }
</style>
</head>
<body>
<main class="menu">

  <header class="masthead">
    <div class="masthead__right"></div>
    <div class="pan-art" role="img" aria-label="Illustration of fried eggs in a frying pan"></div>
    <h1 class="brand"><span class="brand__the">The</span><span class="brand__name">Marlowbrook</span></h1>
    <div class="headline">Breakfast<br><span class="amp">&amp;</span>Lunch</div>
    <div class="served">Served Untill 5.00 pm</div>
    <div class="plate-art" role="img" aria-label="Illustration of a plate with toast, avocado and egg"></div>
  </header>

  <section class="col-head col-head--breakfast">
    <h2>Breakfast’s</h2>
    <div class="icon-art" style="left:240px;top:46px;width:44px;height:34px" role="img" aria-label="Steaming cup icon"></div>
  </section>
  <section class="col-head col-head--build">
    <h2>Build Your<br>Own</h2>
    <svg class="abs" style="left:24px;top:64px" width="46" height="40" viewBox="0 0 46 40" aria-hidden="true">
      <g fill="#fff"><rect x="4" y="8" width="3" height="32"/><ellipse cx="20" cy="12" rx="6" ry="10"/><rect x="18.5" y="18" width="3" height="22"/><path d="M32 2 q6 10 0 20 v18 h-3 V2z"/></g>
    </svg>
    <svg class="abs" style="left:214px;top:64px" width="46" height="40" viewBox="0 0 46 40" aria-hidden="true">
      <g fill="#fff"><path d="M8 2 q6 10 0 20 v18 h-3 V2z"/><ellipse cx="24" cy="12" rx="6" ry="10"/><rect x="22.5" y="18" width="3" height="22"/><rect x="38" y="8" width="3" height="32"/></g>
    </svg>
  </section>
  <section class="col-head col-head--snacks">
    <h2>Snack’s</h2>
    <div class="icon-art" style="left:186px;top:42px;width:62px;height:42px" role="img" aria-label="Burger icon"></div>
  </section>

  <div class="build-panel"></div>

  <p class="intro">All our breakfast ingredients are of the highest quality available, sourced directly from the UK &amp; freshly cooked to order</p>

  <h3 class="set-name" style="top:384px">Marlowbrook</h3>
  <p class="set-desc" style="top:411px">Bacon, Fried Egg, Sausage, Beans or Grilled Tomato, Toast &amp; Butter</p>
  <p class="set-free" style="top:456px">FREE</p>
  <p class="set-drink" style="top:483px"><span>Tea, Coffee or Orange</span><span class="price">4.50</span></p>
  <div class="divider"></div>
  <h3 class="set-name" style="top:530px">Hearty</h3>
  <p class="set-desc" style="top:556px">2 Bacon, 2 Fried Egg, 2 Sausage, Beans or Grilled Tomato, Toast &amp; Butter</p>
  <p class="set-free" style="top:602px">FREE</p>
  <p class="set-drink" style="top:629px"><span>Tea, Coffee or Orange</span><span class="price">6.50</span></p>
  <p class="note">Any changes made to set breakfasts will be charged as build your own</p>

  <ul class="list list--build">
    <li><span>Sausage</span><span class="price">1.00</span></li>
    <li><span>Fried Egg</span><span class="price">0.75</span></li>
    <li><span>Bacon</span><span class="price">1.00</span></li>
    <li><span>Beans</span><span class="price">0.50</span></li>
    <li><span>Black Pudding</span><span class="price">1.00</span></li>
    <li><span>Grilled Tomato</span><span class="price">0.50</span></li>
    <li><span>Fried Bread</span><span class="price">1.00</span></li>
    <li><span>Hash Brown</span><span class="price">0.75</span></li>
    <li><span>Mushrooms</span><span class="price">1.25</span></li>
    <li><span>2 Bread &amp; Butter</span><span class="price">1.00</span></li>
    <li><span>Poached Egg</span><span class="price">1.50</span></li>
    <li><span>2 Toast &amp; Butter</span><span class="price">1.50</span></li>
    <li><span>Scrambled Eggs</span><span class="price">2.00</span></li>
  </ul>
  <div class="min-order">Minimum order of 3.50</div>

  <ul class="list list--snacks">
    <li><span>2 Fried Eggs On Toast</span><span class="price">3.50</span></li>
    <li><span>Sausage Sandwich</span><span class="price">4.00</span></li>
    <li><span>Scrambled Egg On Toast</span><span class="price">3.50</span></li>
    <li><span>Bacon Sandwish</span><span class="price">4.00</span></li>
    <li><span>Poached Egg On Toast</span><span class="price">4.00</span></li>
    <li><span>Fried Egg Sandwich</span><span class="price">3.50</span></li>
    <li><span>Beans On Toast</span><span class="price">3.50</span></li>
    <li><span>Bacon &amp; Egg Sandwich</span><span class="price">4.50</span></li>
    <li><span>Toast &amp; Preserves</span><span class="price">2.50</span></li>
    <li><span>Sausage &amp; Egg Sandwich</span><span class="price">4.50</span></li>
  </ul>
  <div class="deco" style="left:658px;top:616px;width:112px;height:86px;border-radius:10px" role="img" aria-label="Line illustration of a burger and fries"></div>

  <section class="specials" aria-label="Something Different"></section>
  <div class="deco" style="left:142px;top:776px;width:64px;height:60px" role="img" aria-label="Line illustration of a fried egg"></div>
  <div class="deco" style="left:664px;top:792px;width:54px;height:54px" role="img" aria-label="Line illustration of a whisk"></div>
  <h2 class="banner">Something Different??</h2>
  <div class="split"></div>

  <article class="dish dish--left" style="top:870px">
    <h3>Egg Benedict</h3>
    <div class="dish__body"><p>Traditional eggs Benedict with home baked ham &amp; soft poached eggs coated in a rich hollandaise sauce on a toasted english muffin</p><span class="price">5.50</span></div>
  </article>
  <article class="dish dish--left" style="top:976px">
    <h3>Egg Royale</h3>
    <div class="dish__body"><p>Smoked salmon on a toasted english muffin soft poached eggs &amp; a Hollandaise sauce</p><span class="price">6.00</span></div>
  </article>
  <article class="dish dish--left" style="top:1065px">
    <h3>Pancake Stack</h3>
    <div class="dish__body"><p>American Pancakes with Crispy bacon rashers &amp; maple syrup</p><span class="price">6.50</span></div>
  </article>

  <article class="dish dish--right" style="top:870px">
    <h3>Smoked &amp; Scrambled</h3>
    <div class="dish__body"><p>Smoked salmon with creamy scrambled eggs served with wholemeal toast</p><span class="price">6.50</span></div>
  </article>
  <article class="dish dish--right" style="top:959px">
    <h3>Big Breakfast Wrap</h3>
    <div class="dish__body"><p>Sausage, bacon, 2 egg omelette &amp; hash brown in a soft tortilla wrap</p><span class="price">5.50</span></div>
  </article>
  <article class="dish dish--right" style="top:1048px">
    <h3>Breakfast Muffin</h3>
    <div class="dish__body"><p>Bacon or sausage on an english muffin with mature cheddar cheese &amp; topped with a fried egg <span class="aside">( Just like your favourite fast food joint!! )</span></p><span class="price">5.00</span></div>
  </article>

  <div class="deco" style="left:0;top:976px;width:48px;height:40px" role="img" aria-label="Line illustration of a wrap"></div>
  <div class="deco" style="left:272px;top:1130px;width:70px;height:50px" role="img" aria-label="Line illustration of a pancake stack"></div>
  <div class="deco" style="left:790px;top:928px;width:59px;height:44px;border-radius:6px" role="img" aria-label="Line illustration of a cheese wedge"></div>
  <div class="deco" style="left:706px;top:1130px;width:56px;height:62px" role="img" aria-label="Line illustration of a cupcake"></div>

</main>
</body>
</html>
```